4Star Hotel looking for web design

Hello everyone,
We are located in Cambodia, the hotel should open in 2-3 months. The name will be Velmora-Boutique Hotel. We are looking for a webdesign which is professional, elegant and SIMPLE.
All informations should be easy to find. We are quite open to proposition but we would like to the home page:
-a carousel with around 5-8 picture
-Little menu where we can book a room
By the way, we would like a page for our restaurant, gallery, contact page for description of the rooms. I add some old pictures.
I give an example of what we are expecting:
www.quenrostays.com/tovelspring
We hope that we are proposing a good job for you guys. Have fun and Thanks.
Oh and the winner ( or someone he had choose) of course have free night in our presidential suite
Target Market(s)
We are looking for european Market. Let s say people middle age who are willing to travel in difficult area
Industry/Entity Type
Hotel
Coding
Coded - Design and coding required
Number of Pages Required
5+ page
Requirements
Must have
- Simple, simple and Simple
- Carousel
- place for book a room
- during booking, a menu for select room , and after that another menu for propose like tour in town, taxi, flower, bottle of champagne for example
- during all the process, the customer should be able to know at what step it is and can stop and come back after
- Have to be perfect for smartphone
- Price with drawbar for they know how much they earn with our reduction
Nice to have
- during the process of information (name, adress, tel...), it would be great if they can fill it with a button facebook, google plus, lindkdin, instagram ....
- then a button share on facebook, twitter for know that they book in our hotel
- At the end of the booking, a flashcode with the recapitulatif that customer can scan.

```html
<!DOCTYPE html>
<html lang="en">
<head>
<meta charset="utf-8">
<title>Velmora Boutique Hotel – Features</title>
<link href="https://fonts.googleapis.com/css2?family=Open+Sans:wght@400;600;700&display=swap" rel="stylesheet">
<style>
:root{
  --brown:#7b2d12;
  --rust:#8f3b18;
  --orange:#e9a01d;
  --ink:#333333;
  --muted:#777777;
  --line:#e2e2e2;
  --panel:#f3f3f3;
  --white:#ffffff;
}
*{box-sizing:border-box;margin:0;padding:0}
html,body{width:1200px;height:2232px;overflow:hidden;background:var(--white);font-family:"Open Sans",Arial,sans-serif;color:var(--ink)}
.page{position:relative;width:1200px;height:2232px}

.site-header{position:absolute;top:0;left:0;width:1200px;height:112px;background:var(--white)}
.brand{position:absolute;left:88px;top:0;width:156px;height:150px;background:var(--white);z-index:3;text-align:center;padding-top:22px;border-bottom:4px solid var(--brown);box-shadow:0 2px 6px rgba(0,0,0,.15)}
.brand-mark{width:54px;height:54px;margin:0 auto 8px;border-radius:50%;background:var(--brown)}
.brand-name{font-size:22px;font-weight:700;color:var(--brown);line-height:1}
.brand-sub{font-size:11px;color:var(--brown);margin-top:4px}
.brand-stars{font-size:12px;color:var(--orange);letter-spacing:3px;margin-top:4px}
.main-nav{position:absolute;right:96px;top:44px;display:flex;gap:28px;align-items:center;font-size:15px;font-weight:600}
.main-nav a{color:var(--ink);text-decoration:none}
.main-nav a.active{color:var(--orange)}
.search-btn{width:28px;height:28px;border-radius:50%;background:var(--brown);display:flex;align-items:center;justify-content:center}

.hero{position:absolute;top:112px;left:0;width:1200px;height:428px;background:linear-gradient(180deg,#b9c2c6 0%,#8d9aa0 35%,#4d6a3c 60%,#3b5230 80%,#7a3a26 100%)}
.hero-tag{position:absolute;left:50%;transform:translateX(-50%);background:var(--orange);color:var(--white);font-weight:600;letter-spacing:2px;white-space:nowrap;text-align:center}
.hero-tag.one{top:168px;font-size:22px;padding:10px 30px}
.hero-tag.two{top:232px;font-size:22px;padding:10px 34px;background:rgba(233,160,29,.92)}
.hero-arrow{position:absolute;top:196px;width:36px;height:36px;background:rgba(255,255,255,.35);display:flex;align-items:center;justify-content:center}
.hero-arrow.prev{left:70px}.hero-arrow.next{right:70px}

.section-title{position:absolute;left:96px;top:574px;width:1008px;font-size:19px;font-weight:700;padding-bottom:14px;border-bottom:1px solid var(--line)}

.features{position:absolute;left:96px;top:632px;width:750px}
.feature{display:flex;gap:20px;height:220px}
.feature-photo{width:304px;height:188px;flex:none}
.feature-body{padding-top:2px;width:420px}
.feature-body h3{font-size:15px;font-weight:700;line-height:1.45;margin-bottom:10px}
.feature-body p{font-size:12px;color:var(--muted);line-height:1.6}
.feature-body .more{display:block;margin-top:10px;font-size:12px;color:var(--orange);font-weight:600}

.sidebar{position:absolute;left:900px;top:640px;width:212px}
.booking{background:var(--rust);padding:18px 16px 20px}
.booking h4{color:var(--white);font-size:14px;font-weight:700;margin-bottom:14px}
.field{height:30px;background:var(--white);margin-bottom:12px;display:flex;justify-content:space-between;align-items:center;padding:0 10px;font-size:11px;color:var(--muted)}
.book-btn{margin:18px auto 0;width:120px;height:32px;background:var(--orange);color:var(--white);font-size:12px;font-weight:700;display:flex;align-items:center;justify-content:center}
.listing-badge{background:#dcdcdc;margin-top:72px;height:40px;width:180px;border-radius:20px}
.follow-badge{background:#c9cfdc;margin-top:28px;height:82px;width:164px;border-radius:4px}

.contact{position:absolute;left:0;top:2000px;width:1200px;height:172px;background:var(--panel);border-top:4px solid var(--orange)}
.contact h5{position:absolute;left:96px;top:30px;font-size:19px;font-weight:700}
.contact h5 span{color:var(--orange)}
.contact-row{position:absolute;left:96px;top:90px;display:flex;gap:70px;font-size:13px;color:var(--muted);align-items:center}
.contact-item{display:flex;gap:12px;align-items:center}

.site-footer{position:absolute;left:0;top:2172px;width:1200px;height:60px;background:var(--brown);color:#e8d2c7;font-size:11px}
.site-footer .copy{position:absolute;left:96px;top:22px}
.footer-social{position:absolute;right:96px;top:16px;display:flex;gap:8px}
.footer-social span{width:26px;height:26px;background:var(--orange);border-radius:3px}
</style>
</head>
<body>
<div class="page">
  <header class="site-header">
    <div class="brand">
      <div class="brand-mark"></div>
      <div class="brand-name">Velmora</div>
      <div class="brand-sub">Boutique Hotel</div>
      <div class="brand-stars">★★★★</div>
    </div>
    <nav class="main-nav">
      <a href="#">HOME</a><a href="#">ACCOMMODATION</a><a href="#">BLOG</a><a class="active" href="#">FEATURES</a><a href="#">CONTACT US</a>
      <span class="search-btn"><svg width="14" height="14" viewBox="0 0 14 14"><circle cx="6" cy="6" r="4" stroke="#fff" stroke-width="2" fill="none"/><line x1="9" y1="9" x2="13" y2="13" stroke="#fff" stroke-width="2"/></svg></span>
    </nav>
  </header>

  <section class="hero" role="img" aria-label="Carousel photo of the river landscape and town seen from the hotel terrace">
    <div class="hero-tag one">100 % RESPONSIBLE &amp; MOBILE READY</div>
    <div class="hero-tag two">ROOM AVAILABILITY CHECKER AND BOOKING</div>
    <span class="hero-arrow prev"><svg width="14" height="18"><polyline points="11,2 3,9 11,16" stroke="#fff" stroke-width="3" fill="none"/></svg></span>
    <span class="hero-arrow next"><svg width="14" height="18"><polyline points="3,2 11,9 3,16" stroke="#fff" stroke-width="3" fill="none"/></svg></span>
  </section>

  <h2 class="section-title">FEATURES</h2>

  <main class="features">
    <article class="feature"><div class="feature-photo" role="img" aria-label="Photo of the hotel entrance stairway" style="background:linear-gradient(135deg,#6b3a22,#c79a6e)"></div>
      <div class="feature-body"><h3>SED UT PERSPICIATIS UNDE OMNIS ISTE NATUS SIT VOLUPTATEM ACCUSANTIUM</h3><p>Sed ut perspiciatis unde omnis iste natus error sit voluptatem accusantium doloremque laudantium, totam rem aperiam eaque ipsa quae ab illo inventore veritatis et quasi architecto beatae vitae dicta sunt explicabo. Nemo enim ipsam voluptatem quia voluptas sit aspernatur.</p><a class="more">READ MORE</a></div></article>
    <article class="feature"><div class="feature-photo" role="img" aria-label="Photo of a guest room with bed and wardrobe" style="background:linear-gradient(135deg,#8a6a4a,#e5dccd)"></div>
      <div class="feature-body"><h3>SED UT PERSPICIATIS UNDE OMNIS ISTE NATUS SIT VOLUPTATEM ACCUSANTIUM</h3><p>Sed ut perspiciatis unde omnis iste natus error sit voluptatem accusantium doloremque laudantium, totam rem aperiam eaque ipsa quae ab illo inventore veritatis et quasi architecto beatae vitae dicta sunt explicabo. Nemo enim ipsam voluptatem quia voluptas sit aspernatur.</p><a class="more">READ MORE</a></div></article>
    <article class="feature"><div class="feature-photo" role="img" aria-label="Photo of a room corner with a chair by the window" style="background:linear-gradient(135deg,#3e2418,#b08864)"></div>
      <div class="feature-body"><h3>SED UT PERSPICIATIS UNDE OMNIS ISTE NATUS SIT VOLUPTATEM ACCUSANTIUM</h3><p>Sed ut perspiciatis unde omnis iste natus error sit voluptatem accusantium doloremque laudantium, totam rem aperiam eaque ipsa quae ab illo inventore veritatis et quasi architecto beatae vitae dicta sunt explicabo. Nemo enim ipsam voluptatem quia voluptas sit aspernatur.</p><a class="more">READ MORE</a></div></article>
    <article class="feature"><div class="feature-photo" role="img" aria-label="Photo of the hotel building facade" style="background:linear-gradient(180deg,#9fb6c8,#a4563a 60%,#6d3a26)"></div>
      <div class="feature-body"><h3>SED UT PERSPICIATIS UNDE OMNIS ISTE NATUS SIT VOLUPTATEM ACCUSANTIUM</h3><p>Sed ut perspiciatis unde omnis iste natus error sit voluptatem accusantium doloremque laudantium, totam rem aperiam eaque ipsa quae ab illo inventore veritatis et quasi architecto beatae vitae dicta sunt explicabo. Nemo enim ipsam voluptatem quia voluptas sit aspernatur.</p><a class="more">READ MORE</a></div></article>
    <article class="feature"><div class="feature-photo" role="img" aria-label="Photo of a hotel corridor with wooden floor" style="background:linear-gradient(135deg,#7a3a1e,#d2a07a)"></div>
      <div class="feature-body"><h3>SED UT PERSPICIATIS UNDE OMNIS ISTE NATUS SIT VOLUPTATEM ACCUSANTIUM</h3><p>Sed ut perspiciatis unde omnis iste natus error sit voluptatem accusantium doloremque laudantium, totam rem aperiam eaque ipsa quae ab illo inventore veritatis et quasi architecto beatae vitae dicta sunt explicabo. Nemo enim ipsam voluptatem quia voluptas sit aspernatur.</p><a class="more">READ MORE</a></div></article>
    <article class="feature"><div class="feature-photo" role="img" aria-label="Photo of a stone statue in the lobby" style="background:linear-gradient(135deg,#5a4a3e,#cfc4b6)"></div>
      <div class="feature-body"><h3>SED UT PERSPICIATIS UNDE OMNIS ISTE NATUS SIT VOLUPTATEM ACCUSANTIUM</h3><p>Sed ut perspiciatis unde omnis iste natus error sit voluptatem accusantium doloremque laudantium, totam rem aperiam eaque ipsa quae ab illo inventore veritatis et quasi architecto beatae vitae dicta sunt explicabo. Nemo enim ipsam voluptatem quia voluptas sit aspernatur.</p><a class="more">READ MORE</a></div></article>
  </main>

  <aside class="sidebar">
    <form class="booking">
      <h4>BOOKING NOW</h4>
      <div class="field">Arrival<svg width="10" height="6"><polygon points="0,0 10,0 5,6" fill="#555"/></svg></div>
      <div class="field">Departure<svg width="10" height="6"><polygon points="0,0 10,0 5,6" fill="#555"/></svg></div>
      <div class="field">Room<svg width="10" height="6"><polygon points="0,0 10,0 5,6" fill="#555"/></svg></div>
      <div class="field">Adults<svg width="10" height="6"><polygon points="0,0 10,0 5,6" fill="#555"/></svg></div>
      <div class="field">Children<svg width="10" height="6"><polygon points="0,0 10,0 5,6" fill="#555"/></svg></div>
      <div class="book-btn">BOOK NOW</div>
    </form>
    <div class="listing-badge"></div>
    <div class="follow-badge"></div>
  </aside>

  <section class="contact">
    <h5>CONTACT <span>US</span></h5>
    <div class="contact-row">
      <div class="contact-item"><svg width="18" height="24" viewBox="0 0 18 24"><path d="M9 0C4 0 0 4 0 9c0 7 9 15 9 15s9-8 9-15c0-5-4-9-9-9z" fill="#e9a01d"/><circle cx="9" cy="9" r="3.5" fill="#f3f3f3"/></svg><span>1234 Lorem ipsum dolor sit amet,<br>elit eiusmod tempor</span></div>
      <div class="contact-item"><svg width="20" height="20" viewBox="0 0 20 20"><path d="M4 1l4 4-2 3c1 3 3 5 6 6l3-2 4 4-3 3C8 19 1 12 1 4z" fill="#e9a01d"/></svg><span>(123) 456 7890</span></div>
      <div class="contact-item"><svg width="22" height="16" viewBox="0 0 22 16"><rect width="22" height="16" rx="2" fill="#e9a01d"/><polyline points="1,1 11,9 21,1" stroke="#f3f3f3" stroke-width="2" fill="none"/></svg><span>info@velmorahotel.com</span></div>
      <div class="contact-item"><svg width="20" height="20" viewBox="0 0 20 20"><path d="M4 1l4 4-2 3c1 3 3 5 6 6l3-2 4 4-3 3C8 19 1 12 1 4z" fill="#e9a01d"/></svg><span>(123) 456 7890</span></div>
    </div>
  </section>

  <footer class="site-footer">
    <p class="copy">Copyright © 2015 Velmora. All rights reserved.</p>
    <div class="footer-social"><span></span><span></span><span></span><span></span><span></span></div>
  </footer>
</div>
</body>
</html>
```